Packaging design for a reclosable bag for our product

We have a logo, and we need to put it on packaging for our product and while we want the look to be simple, we want it to follow good design principles and also contain spaces for other product descriptions.

There will be 5 sizes at launch so I'd like 5 variations, one for each size.

I've included a few mockups of the type of bag that I made but they are all just rough ideas that I had.

I want the brand to look scientific and methodical and even a bit quirky, as in "wow this is a serious product but also a bit unusual."

```html
<!DOCTYPE html>
<html lang="en">
<head>
<meta charset="utf-8">
<title>Orvo Bias Lighting – Pouch Range</title>
<link rel="stylesheet" href="https://fonts.googleapis.com/css2?family=Nunito:wght@400;800;900&family=Nunito+Sans:wght@300;400&display=swap">
<style>
  :root {
    --page: #ffffff;
    --pouch: #1c1c1c;
    --pouch-strip: #262626;
    --tag-band: #111111;
    --seal-line: #2e2e2e;
    --ink: #ffffff;
    --ink-soft: #e6e6e6;
    --xxl: #7d3b9e;
    --xxl-text: #a040e0;
    --xl: #1a86d0;
    --xl-text: #2a9cf0;
    --l: #ea7a16;
    --l-text: #f08a1e;
    --m: #f6c400;
    --m-text: #f6c400;
    --s: #6aa42e;
    --s-text: #7cc23a;
    --xs: #e0222a;
    --xs-text: #f0262e;
  }
  * { box-sizing: border-box; margin: 0; padding: 0; }
  html, body { width: 1200px; height: 1200px; overflow: hidden; background: var(--page); }
  .range { position: relative; width: 1200px; height: 1200px; }

  .pouch {
    position: absolute;
    width: 292px;
    height: 445px;
    background: var(--pouch);
    border-radius: 12px 12px 2px 2px;
    overflow: hidden;
  }
  .pouch::before {
    content: "";
    position: absolute;
    left: 0; top: 0; bottom: 0;
    width: 50px;
    background: var(--pouch-strip);
  }
  .pouch__seal {
    position: absolute;
    left: 0; right: 0;
    height: 2px;
    background: var(--seal-line);
  }
  .pouch__seal--upper { top: 42px; }
  .pouch__seal--lower { top: 54px; }

  .pouch__tag-band {
    position: absolute;
    left: 3px; top: 279px;
    width: 47px; height: 70px;
    background: var(--tag-band);
  }
  .pouch__tag {
    position: absolute;
    left: 3px; top: 290px;
    width: 47px; height: 47px;
    display: flex; align-items: center; justify-content: center;
    font-family: "Nunito", sans-serif;
    font-weight: 900;
    color: var(--ink);
    font-size: 20px;
    letter-spacing: 0.5px;
  }

  .pouch__label {
    position: absolute;
    left: 60px; top: 236px;
    color: var(--ink);
  }
  .brand {
    font-family: "Nunito", sans-serif;
    font-weight: 900;
    font-size: 40px;
    line-height: 44px;
    letter-spacing: -1px;
  }
  .product {
    font-family: "Nunito", sans-serif;
    font-weight: 800;
    font-size: 20.5px;
    line-height: 24px;
    margin-top: 6px;
  }
  .length {
    font-family: "Nunito Sans", sans-serif;
    font-weight: 400;
    font-size: 12.5px;
    line-height: 16px;
    margin-top: 6px;
  }
  .spec {
    font-family: "Nunito Sans", sans-serif;
    font-weight: 300;
    font-size: 12.5px;
    line-height: 17px;
    color: var(--ink-soft);
    margin-top: 11px;
  }

  .pouch--xxl { left: 99px;  top: 120px; }
  .pouch--xl  { left: 453px; top: 120px; }
  .pouch--l   { left: 811px; top: 120px; }
  .pouch--m   { left: 99px;  top: 640px; }
  .pouch--s   { left: 453px; top: 640px; }
  .pouch--xs  { left: 811px; top: 640px; }

  .pouch--xxl .pouch__tag { background: var(--xxl); font-size: 18px; }
  .pouch--xl  .pouch__tag { background: var(--xl); }
  .pouch--l   .pouch__tag { background: var(--l); }
  .pouch--m   .pouch__tag { background: var(--m); }
  .pouch--s   .pouch__tag { background: var(--s); }
  .pouch--xs  .pouch__tag { background: var(--xs); }

  .pouch--xxl .length { color: var(--xxl-text); }
  .pouch--xl  .length { color: var(--xl-text); }
  .pouch--l   .length { color: var(--l-text); }
  .pouch--m   .length { color: var(--m-text); }
  .pouch--s   .length { color: var(--s-text); }
  .pouch--xs  .length { color: var(--xs-text); }
</style>
</head>
<body>
<main class="range">

  <article class="pouch pouch--xxl">
    <span class="pouch__seal pouch__seal--upper"></span>
    <span class="pouch__seal pouch__seal--lower"></span>
    <span class="pouch__tag-band"></span>
    <span class="pouch__tag">XXL</span>
    <div class="pouch__label">
      <p class="brand">Orvo</p>
      <p class="product">Bias Lighting</p>
      <p class="length">6 Meters / 19.7 Feet</p>
      <p class="spec">White Bias Lighting<br>6500K / Simulated D65 / CRI 95+</p>
    </div>
  </article>

  <article class="pouch pouch--xl">
    <span class="pouch__seal pouch__seal--upper"></span>
    <span class="pouch__seal pouch__seal--lower"></span>
    <span class="pouch__tag-band"></span>
    <span class="pouch__tag">XL</span>
    <div class="pouch__label">
      <p class="brand">Orvo</p>
      <p class="product">Bias Lighting</p>
      <p class="length">5 Meters / 16.4 Feet</p>
      <p class="spec">White Bias Lighting<br>6500K / Simulated D65 / CRI 95+</p>
    </div>
  </article>

  <article class="pouch pouch--l">
    <span class="pouch__seal pouch__seal--upper"></span>
    <span class="pouch__seal pouch__seal--lower"></span>
    <span class="pouch__tag-band"></span>
    <span class="pouch__tag">L</span>
    <div class="pouch__label">
      <p class="brand">Orvo</p>
      <p class="product">Bias Lighting</p>
      <p class="length">4 Meters / 13.1 Feet</p>
      <p class="spec">White Bias Lighting<br>6500K / Simulated D65 / CRI 95+</p>
    </div>
  </article>

  <article class="pouch pouch--m">
    <span class="pouch__seal pouch__seal--upper"></span>
    <span class="pouch__seal pouch__seal--lower"></span>
    <span class="pouch__tag-band"></span>
    <span class="pouch__tag">M</span>
    <div class="pouch__label">
      <p class="brand">Orvo</p>
      <p class="product">Bias Lighting</p>
      <p class="length">3 Meters / 9.8 Feet</p>
      <p class="spec">White Bias Lighting<br>6500K / Simulated D65 / CRI 95+</p>
    </div>
  </article>

  <article class="pouch pouch--s">
    <span class="pouch__seal pouch__seal--upper"></span>
    <span class="pouch__seal pouch__seal--lower"></span>
    <span class="pouch__tag-band"></span>
    <span class="pouch__tag">S</span>
    <div class="pouch__label">
      <p class="brand">Orvo</p>
      <p class="product">Bias Lighting</p>
      <p class="length">2 Meters / 6.6 Feet</p>
      <p class="spec">White Bias Lighting<br>6500K / Simulated D65 / CRI 95+</p>
    </div>
  </article>

  <article class="pouch pouch--xs">
    <span class="pouch__seal pouch__seal--upper"></span>
    <span class="pouch__seal pouch__seal--lower"></span>
    <span class="pouch__tag-band"></span>
    <span class="pouch__tag">XS</span>
    <div class="pouch__label">
      <p class="brand">Orvo</p>
      <p class="product">Bias Lighting</p>
      <p class="length">1 Meter / 3.3 Feet</p>
      <p class="spec">White Bias Lighting<br>6500K / Simulated D65 / CRI 95+</p>
    </div>
  </article>

</main>
</body>
</html>
```